Brantley Gutters 15"x12" EDDM flyer

Brantley Gutter a new seamless gutter company is looking for designs for an Every Door Direct Mailing (EDDM) piece. The dimensions will be 15" long and 12" high. Designs must be submitted with pms colors and be at least 300 dpi.

Brantley Gutters LLC.
The products you need at prices you can afford!!!

Brantley Gutters provides an excellent rain gutter system to protect your property. Our “factory on wheels” will custom fit seamless gutters to your home. Our goal is quality craftsmanship with top-notch service at a competitive price. We take pride in our installations, have excellent customer service and guarantee our products and services.

15% off new gutter installations
$50 off gutter repair
$139.00 gutter clean out special. May be additional fee if more than 100 lf. Single story homes only
$99 and up for gutter tune ups. Reseal all end caps and seems, reattach down spouts and align gutters/downspouts

Telephone number: 904-RAINPRO 904-724-7776 I would like the number on there both ways.

Website: brantleygutters-demo.com

We would like a neat, clean design (nothing to busy). I like the color palate of red, white, blue and black.

I have a preference of not having to buy images. Main reason is after going I'll provide my own images.

residential single family homes

neat and clean that states what we do

• Some play on the BG in Brantley Gutters but must be professional. A lot of our clients will call because their wives no longer want them getting up on ladder.

```html
<!DOCTYPE html>
<html lang="en">
<head>
<meta charset="utf-8">
<title>Brantley Gutters – EDDM Flyer</title>
<link rel="stylesheet" href="https://fonts.googleapis.com/css2?family=Oswald:wght@500;600&family=Saira:wght@400;500;600&display=swap">
<style>
  :root {
    --page-bg: #e6e8eb;
    --brand-blue: #1a8fc6;
    --brand-blue-dark: #1677aa;
    --brand-red: #e8202a;
    --ink: #1d1d1f;
    --white: #ffffff;
    --photo-sky: #cfe0e8;
    --photo-leaf: #4f7f2a;
    --photo-shirt: #23477e;
    --photo-roof: #6f6860;
  }
  html, body {
    margin: 0;
    padding: 0;
    width: 1125px;
    height: 1200px;
    overflow: hidden;
    background: var(--page-bg);
  }
  .flyer {
    position: absolute;
    left: 0;
    top: 150px;
    width: 1125px;
    height: 900px;
    display: block;
  }
  .headline { font-family: "Saira", sans-serif; font-weight: 500; fill: var(--white); }
  .service { font-family: "Saira", sans-serif; font-weight: 400; fill: var(--ink); }
  .note { font-family: "Saira", sans-serif; font-weight: 600; fill: var(--brand-red); }
  .website { font-family: "Saira", sans-serif; font-weight: 600; fill: var(--brand-blue-dark); }
  .brand-name { font-family: "Saira", sans-serif; font-weight: 600; fill: var(--brand-blue-dark); }
  .offer { font-family: "Oswald", sans-serif; font-weight: 500; fill: var(--white); }
  .call { font-family: "Oswald", sans-serif; font-weight: 500; fill: var(--white); }
</style>
</head>
<body>
<svg class="flyer" viewBox="0 0 810 648" xmlns="http://www.w3.org/2000/svg">
  <defs>
    <linearGradient id="photoTone" x1="0" y1="0" x2="1" y2="1">
      <stop offset="0" stop-color="var(--photo-sky)"/>
      <stop offset="0.25" stop-color="var(--photo-leaf)"/>
      <stop offset="0.55" stop-color="var(--photo-shirt)"/>
      <stop offset="0.85" stop-color="var(--photo-roof)"/>
    </linearGradient>
  </defs>

  <!-- hero photo area -->
  <g class="hero-photo" role="img" aria-label="Photo of a gutter installer in a hard hat fastening a gutter under a roof edge with a cordless drill">
    <rect x="0" y="0" width="810" height="648" fill="url(#photoTone)"/>
  </g>

  <!-- sweeping bands -->
  <path class="band-blue" fill="var(--brand-blue)"
        d="M0,412 C140,452 300,448 420,342 C520,252 650,122 810,82 L810,98 C650,138 520,268 420,358 C300,468 140,478 0,440 Z"/>
  <path class="band-red" fill="var(--brand-red)"
        d="M0,440 C140,478 300,468 420,358 C520,268 650,138 810,98 L810,112 C650,152 520,292 420,382 C300,492 140,522 0,502 Z"/>
  <path class="content-panel" fill="var(--white)"
        d="M0,502 C140,522 300,492 420,382 C520,292 650,152 810,112 L810,648 L0,648 Z"/>

  <!-- brand badge -->
  <g class="brand-badge">
    <circle cx="672" cy="193" r="92" fill="var(--white)" stroke="var(--brand-blue)" stroke-width="7"/>
    <text class="brand-name" x="672" y="186" font-size="31" text-anchor="middle">Brantley</text>
    <text class="brand-name" x="672" y="222" font-size="31" text-anchor="middle">Gutters</text>
  </g>

  <!-- services heading -->
  <rect class="services-bar" x="510" y="320" width="300" height="52" fill="var(--brand-blue)"/>
  <text class="headline" x="550" y="357" font-size="32">Our Services</text>

  <!-- services list -->
  <g class="service-list" text-anchor="end">
    <g class="tick" transform="translate(608,392)">
      <circle r="7" fill="none" stroke="var(--brand-red)" stroke-width="1.8"/>
      <path d="M-3.5,0 L-1,3 L4,-3" fill="none" stroke="var(--brand-red)" stroke-width="1.8"/>
    </g>
    <text class="service" x="773" y="399" font-size="20">Gutters Installs</text>
    <g class="tick" transform="translate(604,426)">
      <circle r="7" fill="none" stroke="var(--brand-red)" stroke-width="1.8"/>
      <path d="M-3.5,0 L-1,3 L4,-3" fill="none" stroke="var(--brand-red)" stroke-width="1.8"/>
    </g>
    <text class="service" x="773" y="433" font-size="20">Gutters Repairs</text>
    <g class="tick" transform="translate(609,461)">
      <circle r="7" fill="none" stroke="var(--brand-red)" stroke-width="1.8"/>
      <path d="M-3.5,0 L-1,3 L4,-3" fill="none" stroke="var(--brand-red)" stroke-width="1.8"/>
    </g>
    <text class="service" x="773" y="468" font-size="20">Gutters Cleans</text>
    <g class="tick" transform="translate(561,493)">
      <circle r="7" fill="none" stroke="var(--brand-red)" stroke-width="1.8"/>
      <path d="M-3.5,0 L-1,3 L4,-3" fill="none" stroke="var(--brand-red)" stroke-width="1.8"/>
    </g>
    <text class="service" x="773" y="500" font-size="20">Performs Tune Ups</text>
    <text class="service" x="773" y="525" font-size="20">To Seamless Gutters</text>
    <text class="note" x="773" y="556" font-size="17">We only install 6"</text>
    <text class="note" x="773" y="577" font-size="17">K style gutters.</text>
    <text class="website" x="773" y="597" font-size="15">brantleygutters-demo.com</text>
  </g>

  <!-- call bar -->
  <rect class="call-bar" x="0" y="603" width="810" height="45" fill="var(--brand-blue)"/>
  <g class="phone-icon" transform="translate(494,626)">
    <circle r="13" fill="none" stroke="var(--white)" stroke-width="2.2"/>
    <path d="M-6,-7 L-3,-8 L-1,-3 L-3,-1 C-2,2 1,5 3,5 L5,3 L9,5 L8,8 C2,9 -8,0 -6,-7 Z" fill="var(--white)"/>
  </g>
  <text class="call" x="780" y="635" font-size="22" text-anchor="end">904-RAINPRO <tspan dx="4">•</tspan><tspan dx="8">904-724-7776</tspan></text>

  <!-- offer hexagons -->
  <g class="offer-hex" transform="translate(360,412)">
    <polygon points="0,-78 67,-39 67,39 0,78 -67,39 -67,-39" fill="var(--white)" stroke="var(--brand-blue)" stroke-width="2.5"/>
    <polygon points="0,-70 61,-35 61,35 0,70 -61,35 -61,-35" fill="var(--brand-blue)"/>
    <text class="offer" y="-14" font-size="24" text-anchor="middle">15% OFF</text>
    <text class="offer" y="12" font-size="17" text-anchor="middle">NEW GUTTER</text>
    <text class="offer" y="36" font-size="17" text-anchor="middle">INSTALLATIONS</text>
  </g>
  <g class="offer-hex" transform="translate(125,550)">
    <polygon points="0,-78 67,-39 67,39 0,78 -67,39 -67,-39" fill="var(--white)" stroke="var(--brand-blue)" stroke-width="2.5"/>
    <polygon points="0,-70 61,-35 61,35 0,70 -61,35 -61,-35" fill="var(--brand-blue)"/>
    <text class="offer" y="-14" font-size="24" text-anchor="middle">$50 OFF</text>
    <text class="offer" y="13" font-size="20" text-anchor="middle">GUTTER</text>
    <text class="offer" y="39" font-size="20" text-anchor="middle">REPAIRS</text>
  </g>
  <g class="offer-hex" transform="translate(280,550)">
    <polygon points="0,-78 67,-39 67,39 0,78 -67,39 -67,-39" fill="var(--white)" stroke="var(--brand-blue)" stroke-width="2.5"/>
    <polygon points="0,-70 61,-35 61,35 0,70 -61,35 -61,-35" fill="var(--brand-blue)"/>
    <text class="offer" y="-10" font-size="19" text-anchor="middle">$139.00 FOR</text>
    <text class="offer" y="16" font-size="21" text-anchor="middle">GUTTER</text>
    <text class="offer" y="36" font-size="14" text-anchor="middle">CLEANING*</text>
  </g>
  <g class="offer-hex" transform="translate(438,550)">
    <polygon points="0,-78 67,-39 67,39 0,78 -67,39 -67,-39" fill="var(--white)" stroke="var(--brand-blue)" stroke-width="2.5"/>
    <polygon points="0,-70 61,-35 61,35 0,70 -61,35 -61,-35" fill="var(--brand-blue)"/>
    <text class="offer" y="-27" font-size="19" text-anchor="middle">GUTTER</text>
    <text class="offer" y="-4" font-size="19" text-anchor="middle">TUNE UPS</text>
    <text class="offer" y="19" font-size="19" text-anchor="middle">STARTING</text>
    <text class="offer" y="42" font-size="19" text-anchor="middle">AT $99.</text>
  </g>
</svg>
</body>
</html>
```